Flyer für Lach- und Humorworkshops
Zielgruppe
Ich biete Lach- und Humorworkshops an für Unternehmen und Privatpersonen, für mehr Lebensfreude und Erfolg, ob privat oder im Business.
Aufgabenstellung
- DIN A6
- Textvorgabe im Word kann auch gekürzt werden, je nach Platz auf dem Flyer
- Schlagwörter wie 'Lachen' in der Schrift 'Licorice' so wie auf der Website

```html
<!DOCTYPE html>
<html lang="de">
<head>
<meta charset="utf-8">
<title>Lach-Workshop Flyer – Innenseite</title>
<link rel="stylesheet" href="https://fonts.googleapis.com/css2?family=Licorice&family=Raleway:wght@400;500;700;800&display=swap">
<style>
  :root {
    --gold: #cfae74;
    --gold-dark: #c29f62;
    --cream: #f3e7d9;
    --white: #ffffff;
    --ink: #2f2c2a;
    --ink-soft: #4a4541;
    --photo-a: #d9d6d2;
    --photo-b: #b8a99a;
  }
  * { box-sizing: border-box; margin: 0; padding: 0; }
  html, body { width: 1200px; height: 848px; overflow: hidden; background: var(--white); }
  body { font-family: "Raleway", sans-serif; color: var(--ink); }
  .spread { display: flex; width: 1200px; height: 848px; }
  .panel { width: 400px; height: 848px; position: relative; }
  .script { font-family: "Licorice", cursive; font-weight: 400; text-transform: none; letter-spacing: 0.02em; }

  /* Panel 1 */
  .panel--intro { background: var(--gold); }
  .intro__photo { height: 430px; background: linear-gradient(160deg, var(--photo-a), var(--photo-b) 70%, #f4f2ef); }
  .intro__lead { padding: 40px 34px 0 46px; font-weight: 800; font-size: 17px; line-height: 1.55; text-transform: uppercase; letter-spacing: 0.04em; color: var(--ink); }
  .intro__lead .script { font-size: 46px; line-height: 0.8; margin-right: 4px; }
  .intro__list { list-style: none; padding: 30px 0 0 62px; }
  .intro__list li { font-size: 17px; font-weight: 500; margin-bottom: 17px; position: relative; }
  .intro__list li::before { content: "•"; position: absolute; left: -14px; }

  /* Panel 2 */
  .panel--quote { background: var(--white); text-align: center; }
  .quote__text { padding: 60px 30px 0 30px; font-size: 17.5px; line-height: 1.65; text-transform: uppercase; color: var(--ink-soft); letter-spacing: 0.01em; }
  .quote__text .script { font-size: 50px; color: var(--ink); line-height: 0.7; }
  .quote__art { display: block; margin: 20px auto 0; }
  .quote__claim { font-family: "Licorice", cursive; color: var(--gold); font-size: 58px; line-height: 1.15; letter-spacing: 0.08em; margin-top: 4px; }

  /* Panel 3 */
  .panel--workshop { background: var(--cream); padding: 40px 34px 0 28px; }
  .workshop__title { font-family: "Licorice", cursive; font-weight: 400; font-size: 56px; line-height: 1; letter-spacing: 0.03em; }
  .workshop__text { font-size: 14.6px; line-height: 1.42; margin-top: 10px; color: var(--ink-soft); }
  .workshop__text strong { color: var(--ink); font-weight: 700; }
  .workshop__sub { margin-top: 26px; font-weight: 800; font-size: 15.5px; line-height: 1.25; text-transform: uppercase; }
  .workshop__sub .script { font-size: 46px; line-height: 0.7; margin-right: 4px; }
  .workshop__text .script { font-size: 32px; color: var(--ink); line-height: 0.8; }
  .workshop__text--long { margin-top: 22px; }
</style>
</head>
<body>
<main class="spread">
  <section class="panel panel--intro">
    <div class="intro__photo" role="img" aria-label="Foto: lachende Frau im weissen T-Shirt, liegend"></div>
    <p class="intro__lead"><span class="script">Lachen</span> &amp; Humor lässt sich sehr vielseitig integrieren, kann einen Anlass bereichern oder ergänzen:</p>
    <ul class="intro__list">
      <li>Teambuilding</li>
      <li>Persönlichkeitsentwicklung</li>
      <li>Stressmanagement</li>
      <li>Gesundheit &amp; Wohlbefinden</li>
      <li>Kreaktivität &amp; Innovation</li>
    </ul>
  </section>

  <section class="panel panel--quote">
    <p class="quote__text"><span class="script">Lachen</span> ist nicht nur ein Ausdruck von Freude, es ist gesund für unseren Körper, ausgleichend für unseren Geist und Balsam für unsere Seele..</p>
    <svg class="quote__art" width="340" height="340" viewBox="0 0 340 340" role="img" aria-label="Aquarell-Illustration: lachende Frau mit Blumen im Haar">
      <defs>
        <radialGradient id="artTone" cx="60%" cy="45%" r="65%">
          <stop offset="0" stop-color="#e9ddd6"/>
          <stop offset="0.55" stop-color="#cdb9ad"/>
          <stop offset="1" stop-color="#5f7470"/>
        </radialGradient>
      </defs>
      <circle cx="170" cy="170" r="168" fill="url(#artTone)"/>
    </svg>
    <p class="quote__claim">Lachen ist wie<br>Kurzferien.</p>
  </section>

  <section class="panel panel--workshop">
    <h2 class="workshop__title">Lach-Workshop</h2>
    <p class="workshop__text"><strong>Du suchst eine besondere Teambuilding Aktivität?</strong> Wie wäre es mit einer kurzen Auszeit aus dem Alltag, die lustig, gesund, nachhaltig und sinnvoll ist?<br>In einem <strong>LACH-WORKSHOP</strong> geht es in erster Linie darum, gemeinsam Spass zu haben und ausgiebig zu lachen. Euch erwartet ein abwechslungsreicher Mix aus einfachen, spielerischen und kreativen Übungen.</p>
    <h3 class="workshop__sub"><span class="script">Humor</span> im Business – für ein positives Betriebsklima:</h3>
    <p class="workshop__text workshop__text--long"><span class="script">Lachen ist gesund</span> – das gilt nicht nur für unsere persönliche Gesundheit, sondern auch für ein Unternehmen. Lachen ist eine universelle, positive Form der Kommunikation. <strong>Lachen</strong> ist essentiell für zwischenmenschliche Beziehungen, denn Lachen schafft Vertrauen und Nähe. Wo gelacht wird, fühlen wir uns wohl, der Teamgeist wird gestärkt, Kreativität und Leistungsbereitschaft werden gefördert. Gesunde, zufriedene, motivierte und ausgeglichene Mitarbeitende lösen Herausforderungen viel kreativer und effizienter. Denn nur wer Freude hat bei der Arbeit, ist zu dauerhaften Höchstleistungen fähig.</p>
  </section>
</main>
</body>
</html>
```